Larkspur Ridge Management - Business Cards

I need business cards. My current logo was designed by a designer at this site and I very much like and am happy with the results. I would like a business card that is trendy, unique, current yet professional. I deal with high net worth clients daily

Target Market(s)

Out of state investors looking to get into the rental market in Ohio

Industry/Entity Type

Property Management, Consulting

Contact Information for Business Card

Name, Title (Chief Financial Officer) office phone number (555) 817-3094 website address larkridgemgmt.example

Font styles to use
Sans Serif

Colors
0054AA
0677BA
7BADD7
CADEEF
E8F1F8
0094D4
00A9DD
6FCCEA
C7EBF8
E9F6FB
00AB8E
00BBA5
67D7C9
C6EFE9
E9F9F6

```html
<!DOCTYPE html>
<html lang="en">
<head>
<meta charset="utf-8">
<title>Larkspur Ridge Management – Business Cards</title>
<link rel="stylesheet" href="https://fonts.googleapis.com/css2?family=Montserrat:wght@600;700;800&family=Josefin+Sans:wght@400;600&display=swap">
<style>
  :root {
    --brand-blue: #0054AA;
    --brand-sky: #0094D4;
    --brand-teal: #00AB8E;
    --brand-mist: #E8F1F8;
    --paper: #f7f9fb;
    --backdrop: #ecefef;
    --ink-soft: #3e4654;
    --rule: #CADEEF;
    --emboss: #dde7ef;
  }
  * { margin: 0; padding: 0; box-sizing: border-box; }
  html, body {
    width: 1200px; height: 800px; overflow: hidden;
    background: var(--backdrop);
  }
  .sheet { position: relative; width: 1200px; height: 800px; }
  .card {
    position: absolute; left: 200px; width: 800px; height: 350px;
    background: var(--paper); overflow: hidden;
  }
  .card--front { top: 30px; }
  .card--back { top: 420px; }
  .card__art { position: absolute; inset: 0; width: 800px; height: 350px; }

  .brand {
    position: absolute; inset: 0;
    display: flex; align-items: center; justify-content: center; gap: 16px;
  }
  .brand__mark { width: 22px; height: 22px; background: var(--brand-teal); }
  .brand__name {
    font-family: "Montserrat", sans-serif; font-weight: 800;
    font-size: 34px; line-height: 1.05; color: var(--brand-blue);
    text-transform: uppercase; letter-spacing: 0.5px; text-align: left;
  }

  .person { position: absolute; left: 366px; top: 78px; }
  .person__name {
    font-family: "Montserrat", sans-serif; font-weight: 700;
    font-size: 27px; letter-spacing: 2.5px; color: var(--brand-blue);
  }
  .person__accent { width: 48px; height: 2px; background: var(--brand-teal); margin-top: 8px; }
  .person__title {
    font-family: "Josefin Sans", sans-serif; font-weight: 400;
    font-size: 18px; letter-spacing: 2.4px; color: var(--ink-soft); margin-top: 14px;
  }
  .contact {
    position: absolute; left: 425px; font-family: "Josefin Sans", sans-serif;
    font-weight: 600; font-size: 19px; letter-spacing: 1px; color: var(--brand-blue);
  }
  .contact--phone { top: 202px; }
  .contact--web { top: 260px; }
</style>
</head>
<body>
<main class="sheet">

  <section class="card card--front" aria-label="Business card front">
    <svg class="card__art" viewBox="0 0 800 350" aria-hidden="true">
      <g fill="none" stroke="var(--emboss)" stroke-width="2">
        <polyline points="760,20 600,170 760,330"/>
        <polyline points="800,40 650,170 800,300"/>
        <polyline points="800,90 705,170 800,250"/>
      </g>
      <path d="M42 14 H758 L783 36 V310 L758 333 H42 L17 310 V36 Z"
            fill="none" stroke="var(--brand-blue)" stroke-width="1.5"/>
      <polygon points="12,10 42,10 12,34" fill="var(--brand-teal)"/>
      <polygon points="788,340 758,340 788,316" fill="var(--brand-teal)"/>
    </svg>
    <div class="brand">
      <span class="brand__mark"></span>
      <span class="brand__name">Larkspur Ridge<br>Management</span>
    </div>
  </section>

  <section class="card card--back" aria-label="Business card back">
    <svg class="card__art" viewBox="0 0 800 350" aria-hidden="true">
      <g fill="none" stroke="var(--emboss)" stroke-width="2">
        <polyline points="80,0 270,170 80,350"/>
        <polyline points="120,0 310,170 120,350"/>
        <polyline points="170,0 360,170 170,350"/>
      </g>
      <polygon points="0,49 109,170 0,304" fill="var(--brand-teal)"/>
      <polygon points="0,55 102,170 0,298" fill="var(--brand-blue)"/>
      <polyline points="10,80 90,170 10,260" fill="none" stroke="#ffffff" stroke-width="1"/>

      <path d="M596 13 H760 L784 30 V318 L760 336 H596"
            fill="none" stroke="var(--brand-blue)" stroke-width="1.5"/>
      <polygon points="770,10 790,10 790,30 784,30 784,16 770,16" fill="var(--brand-teal)"/>
      <polygon points="770,340 790,340 790,320 784,320 784,334 770,334" fill="var(--brand-teal)"/>

      <line x1="337" y1="194" x2="337" y2="300" stroke="var(--rule)" stroke-width="1"/>
      <line x1="425" y1="242" x2="667" y2="242" stroke="var(--rule)" stroke-width="1"/>
      <line x1="425" y1="300" x2="667" y2="300" stroke="var(--rule)" stroke-width="1"/>

      <circle cx="383" cy="214" r="18" fill="none" stroke="var(--brand-sky)" stroke-width="1.3"/>
      <path d="M376 205 c-2 2 -2 6 2 11 c4 5 9 7 11 5 l2 -2 l-4 -4 l-2 2 c-2 -1 -5 -4 -6 -6 l2 -2 l-4 -4 Z"
            fill="var(--brand-sky)"/>

      <circle cx="383" cy="272" r="18" fill="none" stroke="var(--brand-sky)" stroke-width="1.3"/>
      <g fill="none" stroke="var(--brand-sky)" stroke-width="1.2">
        <circle cx="383" cy="272" r="9"/>
        <ellipse cx="383" cy="272" rx="4" ry="9"/>
        <line x1="374" y1="272" x2="392" y2="272"/>
        <line x1="376" y1="267" x2="390" y2="267"/>
        <line x1="376" y1="277" x2="390" y2="277"/>
      </g>
    </svg>

    <div class="person">
      <h1 class="person__name">OWEN HARTLEY</h1>
      <div class="person__accent"></div>
      <p class="person__title">CHIEF FINANCIAL OFFICER</p>
    </div>
    <p class="contact contact--phone">(555) 817-3094</p>
    <p class="contact contact--web">larkridgemgmt.example</p>
  </section>

</main>
</body>
</html>
```